Business Card Design Project

- makeup artist business card

- original and creative

- Elegant design

- Feel free to come out with cool designs but stick to being elegant and attractive

- Design relates to makeup

- includes name, occupation, contact numbers, email, website

- regular size business card

- round corner card

- double sided

- on 1 side it should just have the website name in the center " browsandblush.example "

Industry/Entity Type

Business

Requirements
Must have
• Marla Voss
Makeup Artist
USA: +1 (415)872-6410
Singapore: +65 83027715
marlavoss@browsandblush.example
www.browsandblush.example
Should not have
• nothing cartoon looking.
Pictures of makeup being grab from the internet.. Examples: eyes or lips.

```html
<!DOCTYPE html>
<html lang="en">
<head>
<meta charset="utf-8">
<title>Marla Voss — Makeup Artist Business Card</title>
<link rel="stylesheet" href="https://fonts.googleapis.com/css2?family=Great+Vibes&family=Montserrat:wght@700&family=Open+Sans:wght@600&display=swap">
<style>
  :root {
    --page: #ffffff;
    --powder-light: #cdb39a;
    --powder-mid: #bfa388;
    --powder-deep: #a88c72;
    --gold: #ffb400;
    --violet: #4a0a9e;
    --violet-line: #5a1fb0;
    --white: #ffffff;
  }
  * { margin: 0; padding: 0; box-sizing: border-box; }
  html, body {
    width: 1050px;
    height: 1200px;
    overflow: hidden;
    background: var(--page);
  }
  .sheet {
    position: relative;
    width: 1050px;
    height: 1200px;
  }
  .card {
    position: absolute;
    left: 0;
    width: 1050px;
    height: 600px;
    border-radius: 135px;
    overflow: hidden;
  }
  .card--front { top: 0; }
  .card--back { top: 600px; }
  .powder-texture {
    position: absolute;
    inset: 0;
    background:
      radial-gradient(ellipse at 30% 40%, var(--powder-light), transparent 60%),
      radial-gradient(ellipse at 75% 70%, var(--powder-deep), transparent 65%),
      linear-gradient(160deg, var(--powder-light), var(--powder-mid) 55%, var(--powder-deep));
  }
  .outlined-script {
    font-family: "Great Vibes", cursive;
    color: var(--gold);
    text-shadow:
      1.5px 0 0 var(--violet), -1.5px 0 0 var(--violet),
      0 1.5px 0 var(--violet), 0 -1.5px 0 var(--violet),
      2px 3px 3px rgba(60, 30, 0, 0.45);
    white-space: nowrap;
  }
  .artist-name {
    position: absolute;
    left: 24px;
    top: 214px;
    font-size: 92px;
    font-weight: 400;
    line-height: 1;
  }
  .occupation {
    position: absolute;
    left: 70px;
    top: 311px;
    font-family: "Montserrat", sans-serif;
    font-weight: 700;
    font-size: 33px;
    letter-spacing: 0.5px;
    color: var(--violet);
    text-shadow: 0 0 2px rgba(255, 255, 255, 0.6);
    white-space: nowrap;
  }
  .divider-rule {
    position: absolute;
    left: 470px;
    top: 305px;
    width: 580px;
    height: 3px;
    background: var(--violet-line);
  }
  .contact {
    position: absolute;
    font-family: "Open Sans", sans-serif;
    font-weight: 600;
    color: var(--white);
    text-shadow: 1px 2px 2px rgba(60, 30, 0, 0.55);
    white-space: nowrap;
  }
  .contact .accent { color: var(--gold); }
  .contact--email {
    right: 48px;
    top: 262px;
    font-size: 28px;
  }
  .contact--phones {
    right: 10px;
    top: 312px;
    font-size: 25px;
    word-spacing: 1px;
  }
  .website {
    position: absolute;
    left: 0;
    right: 0;
    top: 240px;
    text-align: center;
    font-size: 92px;
    line-height: 1;
  }
</style>
</head>
<body>
  <main class="sheet">
    <section class="card card--front">
      <div class="powder-texture" role="img" aria-label="Close-up of loose beige face powder texture"></div>
      <h1 class="artist-name outlined-script">Marla Voss</h1>
      <p class="occupation">MAKEUP ARTIST</p>
      <div class="divider-rule"></div>
      <p class="contact contact--email">marlavoss@<span class="accent">browsandblush.example</span></p>
      <p class="contact contact--phones">USA <span class="accent">+1 (415)872-6410</span>&nbsp; Singapore <span class="accent">+65 83027715</span></p>
    </section>
    <section class="card card--back">
      <div class="powder-texture" role="img" aria-label="Close-up of loose beige face powder texture"></div>
      <p class="website outlined-script">www.browsandblush.example</p>
    </section>
  </main>
</body>
</html>
```